Project: Graphic Design Collateral for SCT Next Circle Y2K Event
Client: Solbrook Care Trust Next Circle
Date: September 19, 2025
Time: 6:00 PM - 10:00 PM
Location: TENZO, 4375 Pelham Crest Rd, 2nd Fl, Honolulu, HI 96827
Theme: Y2K
Objective:
To create visually engaging and on-brand graphic design collateral that effectively communicates the theme and excitement of the SCT Next Circle Y2K Event.

Target Market(s)

Young professionals, ages 21-40, interested in supporting the Solbrook Care Trust.

Industry/Entity Type

Healthcare

Requirements
Must have
• Collateral Requirements: • Invitation: o Digital and printable versions o Include event details (date, time, location, RSVP information) o Incorporate Y2K aesthetic (e.g., bold colors, chunky fonts, digital effects) Theming: Embrace the Y2K aesthetic with a focus on iconic technology of the era and gender-neutral visuals. Think shimmering ZUP chat boxes, witty away messages, and the iconic Panelia screen saver with the flying-over-green-hills-cow. Incorporate these elements into the design in a playful and inclusive way. For example, use a stylized chat box as a frame for event information or create social media graphics that mimic the look of early internet interfaces. This approach will not only evoke nostalgia but also add a unique and interactive dimension to the event's branding. Key takeaways: • Focus on iconic Y2K technology: ZUP chat boxes, away messages, Panelia screen saver. • Incorporate technology in a playful and inclusive way: Use as design elements, social media graphics. • Evoke nostalgia and add a unique dimension to the event's branding. • Typography: o Using the ZAP! Gold Groove Jukebox Hits look and feel. Utilize a mix of bold, chunky fonts reminiscent of early 2000s design (e.g., Impact, Arial Black) o Consider using a more modern font for readability and contrast.

```html
<!DOCTYPE html>
<html lang="en">
<head>
<meta charset="utf-8">
<title>SCT Next Circle Y2K Event</title>
<link rel="stylesheet" href="https://fonts.googleapis.com/css2?family=Permanent+Marker&family=Patrick+Hand&family=Luckiest+Guy&display=swap">
<style>
  :root {
    --plum: #2b1119;
    --paper: #ffffff;
    --ink: #141414;
    --white: #ffffff;
    --yellow: #f7ec1c;
    --pink: #f03a9a;
    --coral: #f26a4b;
    --shirt-blue: #9fd4ef;
    --skin: #f6dccb;
    --hair: #c9a56b;
    --hair-dark: #6b4a2e;
  }
  * { margin: 0; padding: 0; box-sizing: border-box; }
  html, body { width: 1200px; height: 1200px; overflow: hidden; background: var(--paper); }
  .invite {
    position: relative; width: 1200px; height: 1200px; background: var(--paper);
    font-family: "Patrick Hand", "Comic Sans MS", cursive; color: var(--ink);
  }
  .header-band {
    position: absolute; left: 0; top: 0; width: 1200px; height: 337px;
    background: var(--plum); text-align: center; color: var(--white);
  }
  .client-name {
    position: absolute; top: 40px; width: 100%;
    font-size: 40px; letter-spacing: 2px;
  }
  .event-title {
    position: absolute; top: 112px; width: 100%;
    font-family: "Permanent Marker", "Arial Black", Impact, sans-serif;
    font-size: 96px; line-height: 1; letter-spacing: 2px; font-weight: 900;
  }
  .event-title .accent-yellow { color: var(--yellow); }
  .event-title .accent-pink { color: var(--pink); }
  .audience {
    position: absolute; top: 262px; width: 100%;
    font-size: 38px; letter-spacing: 2px;
  }
  .guests { position: absolute; opacity: .85; border-radius: 40px 40px 0 0; }
  .guests--left {
    left: 18px; top: 451px; width: 340px; height: 486px;
    background: linear-gradient(180deg, var(--hair) 0%, var(--skin) 35%, var(--shirt-blue) 75%, var(--paper) 100%);
  }
  .guests--right {
    left: 842px; top: 398px; width: 346px; height: 504px;
    background: linear-gradient(180deg, var(--hair-dark) 0%, var(--skin) 35%, #f3f3f3 75%, var(--paper) 100%);
  }
  .theme-mark {
    position: absolute; left: 370px; top: 450px; width: 460px; text-align: center;
    font-family: "Luckiest Guy", "Arial Black", Impact, sans-serif; font-weight: 900;
    font-size: 200px; line-height: 1; letter-spacing: -4px;
    -webkit-text-stroke: 4px var(--ink);
  }
  .theme-mark .y { color: var(--pink); }
  .theme-mark .twok { color: var(--coral); }
  .theme-badge {
    position: absolute; left: 431px; top: 717px; width: 366px; height: 226px;
    background: var(--ink); display: flex; align-items: center; justify-content: center;
    font-family: "Luckiest Guy", "Arial Black", Impact, sans-serif; font-weight: 900;
    font-size: 120px; line-height: 1; color: var(--yellow);
  }
  .details { position: absolute; font-size: 34px; letter-spacing: 2px; white-space: nowrap; }
  .details--place { left: 521px; top: 960px; }
  .details--date { left: 234px; top: 1012px; }
  .footer-band {
    position: absolute; left: 0; top: 1066px; width: 1200px; height: 134px;
    background: var(--plum); color: var(--white); font-size: 34px; letter-spacing: 2px;
  }
  .venue { position: absolute; left: 387px; top: 20px; white-space: nowrap; }
  .rsvp { position: absolute; left: 387px; top: 68px; white-space: nowrap; }
</style>
</head>
<body>
<main class="invite">
  <header class="header-band">
    <p class="client-name">Solbrook Care Trust</p>
    <h1 class="event-title">NEXT <span class="accent-yellow">CI</span><span class="accent-pink">RCLE</span></h1>
    <p class="audience">for young professionals ages 21 to 40</p>
  </header>

  <div class="guests guests--left" role="img" aria-label="Sketched illustration of three young guests in casual shirts"></div>
  <div class="guests guests--right" role="img" aria-label="Sketched illustration of two young guests, one wearing a pink tie"></div>

  <div class="theme-mark"><span class="y">Y</span><span class="twok">2K</span></div>
  <div class="theme-badge">Y2K</div>

  <p class="details details--place">HONOLULU, HI 96827</p>
  <p class="details details--date">SEPTEMBER 19, 2025 ... 6:00 PM – 10:00 PM</p>

  <footer class="footer-band">
    <p class="venue">TENZO: 4375 Pelham Crest Rd, 2nd Fl</p>
    <p class="rsvp">RSVP by September 12</p>
  </footer>
</main>
</body>
</html>
```